Real Estate Agent Service Brochure

I need a trifold brochure to showcase my real estate services. I am a veteran Real Estate Broker specializing in marketing properties for sale and for top dollar. I would like to see designs that use colors from my logo (attached) and I would like to showcase some before and after photos of staging jobs I have done to homes to get them ready for the market. This brochure is specific to home sellers. You are happy to go check out my website for inspiration www.lomavertpa.com but keep the copy as I have written it. The the final design should communicate experienced professional who uses current technologies and strategies to market properties for the highest value.

Target Market(s)

Homeowners wanting to sell their homes

Industry/Entity Type

Real Estate Agent

Font styles to use
Serif

Requirements
Must have
• My, logo, personal photo, title and contact information as listed:
• Marta Venholt
• Owner Broker
• Stager Re-Designer
• 860-912-7048
• BRAVE Realty LLC
• LOMAVERTPA.com
• Marta@LOMAVERTPA.com
• The colors used should be those in my logo.
• Brochure should be able to fit in standard envelope for mailing.
Nice to have
• I think I would like my personal photo and contact information on the front panel.
Should not have
• Bright colors.

```html
<!DOCTYPE html>
<html lang="en">
<head>
<meta charset="utf-8">
<title>BRAVE Realty LLC – Seller Brochure</title>
<link rel="stylesheet" href="https://fonts.googleapis.com/css2?family=Open+Sans:ital,wght@0,400;0,600;0,700;1,600&family=Pinyon+Script&display=swap">
<style>
  :root{
    --navy:#15184f;
    --navy-deep:#0c0f3c;
    --navy-soft:#23276a;
    --paper:#f5f5f4;
    --paper-shade:#e6e6e4;
    --ink:#1f1f24;
    --white:#ffffff;
    --backdrop:#e4e1dc;
    --photo-warm-a:#d8c2a4;
    --photo-warm-b:#5d4a3a;
    --photo-cool-a:#e9e7e3;
    --photo-cool-b:#8e8477;
    --portrait-a:#b9b3ad;
    --portrait-b:#24242c;
  }
  *{box-sizing:border-box;margin:0;padding:0}
  html,body{width:1200px;height:1200px;overflow:hidden}
  body{background:var(--backdrop);font-family:"Open Sans",Arial,sans-serif;color:var(--ink);position:relative}

  .spread{position:absolute;left:210px;width:780px;height:580px;box-shadow:0 4px 14px rgba(0,0,0,.18);overflow:hidden}
  .spread-outside{top:12px;background:var(--navy)}
  .spread-inside{top:608px;background:var(--paper)}
  .spread-art{position:absolute;inset:0;width:780px;height:580px}

  /* outside – logo */
  .brand{position:absolute;left:520px;top:38px;width:260px;text-align:center;color:var(--navy);font-weight:700}
  .brand-name{display:inline-flex;align-items:center;gap:7px;font-size:30px;letter-spacing:1px;line-height:1}
  .brand-name::before{content:"";width:12px;height:12px;background:var(--navy)}
  .brand-sub{display:block;font-size:8px;letter-spacing:4px;margin-top:5px}

  /* outside – middle panel */
  .pitch{position:absolute;left:260px;top:315px;width:260px;text-align:center;color:var(--white)}
  .pitch-title{font-size:12.5px;font-weight:600;margin-bottom:14px}
  .pitch-copy{font-size:10px;line-height:19px;padding:0 22px}
  .pitch-copy em{font-weight:700}

  /* outside – contact */
  .agent-name{position:absolute;left:530px;top:333px;font-family:"Pinyon Script",cursive;font-size:17px;color:var(--white)}
  .agent-roles{position:absolute;left:534px;top:358px;list-style:none;font-size:8.2px;line-height:11px;color:var(--white)}
  .agent-roles li::before{content:"◆";font-size:5px;margin-right:4px;vertical-align:2px}
  .contact{position:absolute;left:560px;top:448px;color:var(--white)}
  .contact-line{display:flex;align-items:center;gap:6px}
  .contact-phone{font-size:15px;font-weight:600;letter-spacing:.4px}
  .contact-mail{font-size:10px;font-weight:600;margin-top:6px}
  .contact-line svg{fill:var(--white);flex:none}

  /* before/after labels */
  .ba-label{position:absolute;font-size:7.5px;font-weight:700;letter-spacing:.3px;text-align:center;width:60px}
  .ba-label.before{color:var(--white)}
  .ba-label.after{color:var(--navy)}

  /* inside – left panel */
  .seller-panel{position:absolute;left:0;top:0;width:260px;height:580px;background:linear-gradient(90deg,var(--navy-deep),var(--navy) 85%,var(--navy-soft));color:var(--white);padding:22px 22px 0 30px}
  .seller-panel p{font-size:7.7px;line-height:10.3px;font-weight:600;text-align:justify;margin-bottom:12px}
  .ba-toggle{display:flex;width:118px;margin:14px auto 8px;border:1.5px solid var(--white);border-radius:10px;overflow:hidden;font-size:8px;font-weight:700}
  .ba-toggle span{flex:1;text-align:center;padding:2px 0}
  .ba-toggle .toggle-before{color:var(--white)}
  .ba-toggle .toggle-after{background:var(--white);color:var(--navy)}
  .staging-grid{display:grid;grid-template-columns:1fr 1fr;grid-auto-rows:59px;gap:3px;margin-left:-6px}
  .staging-photo{background:linear-gradient(160deg,var(--photo-warm-a),var(--photo-warm-b))}
  .staging-photo.after{background:linear-gradient(160deg,#efd7ae,#7a5f45)}

  /* inside – testimonial panels */
  .reviews{position:absolute;top:0;height:580px;width:260px;padding:16px 12px 0 12px}
  .reviews-mid{left:260px;background:linear-gradient(90deg,var(--paper) 80%,var(--paper-shade))}
  .reviews-right{left:520px;background:linear-gradient(90deg,#fbfbfa,var(--paper))}
  .reviews-head{position:relative;font-size:11px;font-weight:700;color:var(--navy);text-align:center;line-height:15px;padding:4px 26px 8px}
  .reviews-head .quote{position:absolute;font-size:30px;line-height:1;font-family:Georgia,serif}
  .reviews-head .q-open{left:6px;top:-2px}
  .reviews-head .q-close{right:6px;bottom:-12px}
  .review{border:1.5px solid var(--navy);border-radius:5px;padding:4px 6px 3px;margin-bottom:7px;font-size:7.2px;line-height:9.5px;text-align:justify;background:var(--white)}
  .review-foot{display:flex;justify-content:space-between;align-items:center;margin-top:2px}
  .review-by{font-weight:700;font-style:italic}
  .stars{color:var(--navy);letter-spacing:1px;font-size:8px}
  .brand-small{text-align:right;color:var(--navy);font-weight:700;margin:2px 4px 10px 0}
  .brand-small .brand-name{font-size:19px;gap:5px}
  .brand-small .brand-name::before{width:8px;height:8px}
  .brand-small .brand-sub{font-size:5px;letter-spacing:2.5px;margin-top:2px}
  .divider{border:0;border-top:2px dotted var(--navy);margin:14px 6px 12px}
  .about p{font-size:7.3px;line-height:9.8px;text-align:justify;margin:0 6px 10px}
</style>
</head>
<body>

<!-- OUTSIDE SPREAD -->
<section class="spread spread-outside" aria-label="Brochure outside">
  <svg class="spread-art" viewBox="0 0 780 580" aria-hidden="false">
    <defs>
      <linearGradient id="panelNavy" x1="0" x2="1">
        <stop offset="0" stop-color="#0c0f3c"/><stop offset="1" stop-color="#1c2061"/>
      </linearGradient>
      <linearGradient id="kitchen" x1="0" y1="0" x2="1" y2="1">
        <stop offset="0" stop-color="#f1efeb"/><stop offset=".55" stop-color="#c9bfb2"/><stop offset="1" stop-color="#7e7063"/>
      </linearGradient>
      <linearGradient id="warm" x1="0" y1="0" x2="0" y2="1">
        <stop offset="0" stop-color="#dcc7aa"/><stop offset="1" stop-color="#4e3d30"/>
      </linearGradient>
      <linearGradient id="bright" x1="0" y1="0" x2="0" y2="1">
        <stop offset="0" stop-color="#eeeae4"/><stop offset="1" stop-color="#7c6b5b"/>
      </linearGradient>
      <linearGradient id="portrait" x1="0" y1="0" x2="0" y2="1">
        <stop offset="0" stop-color="#c4bfb9"/><stop offset=".45" stop-color="#9b948d"/><stop offset="1" stop-color="#22222a"/>
      </linearGradient>
    </defs>

    <rect width="780" height="580" fill="var(--navy)"/>
    <rect width="260" height="580" fill="url(#panelNavy)"/>
    <rect x="258" width="3" height="580" fill="#0a0c33" opacity=".6"/>
    <rect x="519" width="2" height="580" fill="#0a0c33" opacity=".5"/>

    <!-- before / after frames -->
    <g>
      <rect x="27" y="22" width="216" height="266" fill="none" stroke="#fff" stroke-width="2"/>
      <rect x="30" y="25" width="210" height="129" fill="url(#warm)" role="img" aria-label="Photo of a kitchen and stairway before staging"/>
      <rect x="30" y="154" width="210" height="131" fill="url(#bright)" role="img" aria-label="Photo of the dining area and stairway after staging"/>
      <path d="M100 154 L135 124 L170 154 Z" fill="var(--navy)"/>
      <path d="M100 154 L135 184 L170 154 Z" fill="#fff"/>

      <rect x="27" y="297" width="216" height="262" fill="none" stroke="#fff" stroke-width="2"/>
      <rect x="30" y="300" width="210" height="127" fill="url(#warm)" role="img" aria-label="Photo of an empty living room with stone fireplace before staging"/>
      <rect x="30" y="427" width="210" height="129" fill="url(#bright)" role="img" aria-label="Photo of the furnished living room with fireplace after staging"/>
      <path d="M100 427 L135 397 L170 427 Z" fill="var(--navy)"/>
      <path d="M100 427 L135 457 L170 427 Z" fill="#fff"/>
    </g>

    <!-- hero photo -->
    <path d="M260 0 H780 V300 L520 345 Q420 250 260 225 Z" fill="url(#kitchen)" role="img" aria-label="Photo of a bright staged kitchen and dining room"/>
    <!-- logo chevron -->
    <path d="M520 0 H780 V95 L652 152 L520 108 Z" fill="#fff"/>
    <!-- portrait -->
    <rect x="612" y="228" width="168" height="210" fill="url(#portrait)" role="img" aria-label="Portrait photo of broker Marta Venholt"/>
    <!-- swoosh -->
    <path d="M520 400 Q640 446 780 436 V580 H520 Z" fill="var(--navy)"/>
    <path d="M520 398 Q640 444 780 434" fill="none" stroke="#fff" stroke-width="3"/>
  </svg>

  <span class="ba-label before" style="left:105px;top:140px">BEFORE</span>
  <span class="ba-label after" style="left:105px;top:158px">AFTER</span>
  <span class="ba-label before" style="left:105px;top:413px">BEFORE</span>
  <span class="ba-label after" style="left:105px;top:431px">AFTER</span>

  <div class="brand" aria-label="BRAVE Realty LLC">
    <span class="brand-name">BRAVE</span>
    <span class="brand-sub">REALTY LLC</span>
  </div>

  <div class="pitch">
    <h2 class="pitch-title">Proven Market Knowledge</h2>
    <p class="pitch-copy">That’s what you can expect when you work with seasoned specialist <em>Marta Venholt</em> for all your Real Estate needs. The sale of a home is too important an undertaking to entrust to just anyone. Select a dedicated, service-oriented and results-driven broker who understands the intricacies of the Real Estate process...select <em>Marta Venholt</em>.</p>
  </div>

  <p class="agent-name">Marta Venholt</p>
  <ul class="agent-roles">
    <li>Broker Owner</li>
    <li>Stager Re-Designer</li>
  </ul>

  <div class="contact">
    <p class="contact-line contact-phone">
      <svg width="11" height="13" viewBox="0 0 24 24" aria-hidden="true"><path d="M6.6 10.8a15 15 0 006.6 6.6l2.2-2.2c.3-.3.7-.4 1-.2 1.1.4 2.3.6 3.6.6.6 0 1 .4 1 1V20c0 .6-.4 1-1 1A17 17 0 013 4c0-.6.4-1 1-1h3.5c.6 0 1 .4 1 1 0 1.3.2 2.5.6 3.6.1.3 0 .7-.2 1z"/></svg>
      860-912-7048
    </p>
    <p class="contact-line contact-mail">
      <svg width="10" height="8" viewBox="0 0 20 14" aria-hidden="true"><path d="M0 0h20v14H0z M1.5 1.5 10 8l8.5-6.5" fill="#fff" stroke="var(--navy)" stroke-width="1.4"/></svg>
      Marta@LOMAVERTPA.com
    </p>
  </div>
</section>

<!-- INSIDE SPREAD -->
<section class="spread spread-inside" aria-label="Brochure inside">
  <div class="seller-panel">
    <p>Selling Real Estate has changed drastically in the last few years. Today’s real estate processes are multi-faceted undertakings that encompass significant emotional and financial components. Having the right marketing partner is so important; one who works to protect your best interests while capably navigating you through the many complexities of the real estate transaction is vital.</p>
    <p>Marta Venholt Real Estate Marketing Specialist truly understands not only the legal process needed but also recognizes buyer trends and knows how to “showcase” a property to sell targeted to the proper consumer demographic.</p>
    <p>A home is one of your most valuable assets. If you are thinking about selling a property, it is crucial that you hire someone with an extraordinary history of happy sellers.</p>
    <div class="ba-toggle"><span class="toggle-before">BEFORE</span><span class="toggle-after">AFTER</span></div>
    <div class="staging-grid">
      <div class="staging-photo" role="img" aria-label="Basement family room before staging"></div>
      <div class="staging-photo after" role="img" aria-label="Basement family room after staging"></div>
      <div class="staging-photo" role="img" aria-label="Bedroom before staging"></div>
      <div class="staging-photo after" role="img" aria-label="Bedroom after staging"></div>
      <div class="staging-photo" role="img" aria-label="Master bedroom before staging"></div>
      <div class="staging-photo after" role="img" aria-label="Master bedroom after staging"></div>
      <div class="staging-photo" role="img" aria-label="Kitchen before staging"></div>
      <div class="staging-photo after" role="img" aria-label="Kitchen and dining area after staging"></div>
    </div>
  </div>

  <div class="reviews reviews-mid">
    <h3 class="reviews-head"><span class="quote q-open">“</span>This is what Marta's clients say about their experiences:<span class="quote q-close">”</span></h3>
    <article class="review">In the Real Estate Business there are many, but none like Marta. She brings a level of professionalism far above other Brokers. She will have no trouble selling your house. What is different is her honesty, sincerity, and unquestionable ethics. She will make sure that you are satisfied with every aspect of your transaction.
      <div class="review-foot"><span class="review-by">- Warren T.</span><span class="stars">★★★★★</span></div></article>
    <article class="review">Marta and the team at BRAVE are knowledgeable and professional. I have been involved in three separate real estate transactions with Marta as my broker. I am always pleased and impressed by her negotiating skills, her market knowledge and her ability to manage the process.
      <div class="review-foot"><span class="review-by">- Lorna P.</span><span class="stars">★★★★★</span></div></article>
    <article class="review">Am so glad that we found Marta to help us in staging a property that we had just finished renovating. She listened to our ideas of what we envisioned in the spaces based on the style of the house and put it all together and on time for the first open house that got rave reviews! Her combined background in real estate and interior design made her a perfect partner for our job.
      <div class="review-foot"><span class="review-by">- Helga S.</span><span class="stars">★★★★★</span></div></article>
    <article class="review">The marketing and staging of our house was on point. I don't think the sale of our home would have been as successful without it.
      <div class="review-foot"><span class="review-by">- Rob &amp; Tessa K.</span><span class="stars">★★★★★</span></div></article>
    <article class="review">I have had several real estate dealings with Marta each one was handled professionally and with my best interest in mind. Her marketing skills are top notch she made sure my properties where ready for market and showcased them in the best way by staging them and having professional photography done. She helped me get through home inspections issues keeping the sales in tact. I keep using her services and recommend her to family and friends she really knows her stuff!
      <div class="review-foot"><span class="review-by">- Celine A.</span><span class="stars">★★★★★</span></div></article>
  </div>

  <div class="reviews reviews-right">
    <div class="brand-small" aria-label="BRAVE Realty LLC">
      <span class="brand-name">BRAVE</span>
      <span class="brand-sub">REALTY LLC</span>
    </div>
    <article class="review">Marta worked with our builder to help us design new floor plans, she was responsible for all the selections/finishes and then completely staged and decorated the homes using some furniture from old models and also shopping for new furniture. The model homes came out beautiful! The feedback was amazing and all the homes sold quickly! She was responsive with updates and reports. We will be using her services again for our next project!
      <div class="review-foot"><span class="review-by">- Gareth L.</span><span class="stars">★★★★★</span></div></article>
    <article class="review">Marta directed us right from the beginning by preparing a market evaluation using current data, helping us to establish a proper list price; she prepared our property for the market by staging it and then marketed it with great photography and video tours. Because of her pre-marketing preparations we received several offers on our house! Keeping our interests first, Marta negotiated the best deal for us; we were truly blown away by her knowledge, work ethic and professionalism.
      <div class="review-foot"><span class="review-by">- Sam &amp; Ida V.</span><span class="stars">★★★★★</span></div></article>
    <hr class="divider">
    <div class="about">
      <p>Marta devotes her efforts to selling real estate, by keeping up with the evolving market, researching buyer trends and preparing homes before they enter the market by staging them to connect with the target buyer. Marta knows all sales are not alike. Therefore, taking a cookie cutter approach is not acceptable, she recognizes that each property is unique and requires a personalized marketing plan and strategy.</p>
      <p>A veteran in the real estate industry with nearly 30 years expertise and consistent membership in the Multi-Million-Dollar Club combined with her HSC Home Stager and Re-Designer credentials assures that her clients get the advantage of vast knowledge, seasoned experience and proven results, all geared to creating beautiful spaces, which form a connection with the right buyer producing the highest and best offer.</p>
    </div>
  </div>
</section>

</body>
</html>
```